Estate Agent A5 Doublesided leaflet

We would like to have a very vibrant, simple, elegant and memorable leaflet promoting our sales division launch and the special offer of only 0.5% fee for instructions received in March 2015

Target Market(s)

Our customers usually have properties valued 500,000USD or more

Industry/Entity Type

Sales

Requirements
Must have
• originality, easy to remember, clear message to client
Something unique, as in the leaflet attached below

```html
<!DOCTYPE html>
<html lang="en">
<head>
<meta charset="utf-8">
<title>Halden Sales &amp; Lettings – Leaflet</title>
<link rel="stylesheet" href="https://fonts.googleapis.com/css2?family=Arimo:wght@400;700&family=Titillium+Web:wght@700;900&family=Marcellus&display=swap">
<style>
  :root{
    --backdrop:#dedede;
    --paper:#ffffff;
    --brand-green:#1d4d2c;
    --forest:#1b5a33;
    --forest-deep:#154a29;
    --leaf:#138a43;
    --leaf-light:#16974a;
    --orange:#f5a11c;
    --orange-deep:#ef8a12;
    --grey-text:#8c8c8c;
    --grey-dark:#6b6b6b;
    --rule:#b9b9b9;
  }
  *{margin:0;padding:0;box-sizing:border-box}
  html,body{width:1200px;height:1000px;overflow:hidden}
  body{background:var(--backdrop);font-family:"Arimo",Arial,sans-serif;position:relative}
  .page{position:absolute;top:150px;width:479px;height:680px;background:var(--paper);overflow:hidden}
  .page--front{left:96px}
  .page--back{left:625px}
  .abs{position:absolute}

  .brand{display:flex;align-items:center;gap:8px;color:var(--brand-green);font-weight:700;font-size:28px;letter-spacing:-0.5px;line-height:1}
  .brand__square{width:40px;height:40px;background:var(--brand-green)}

  /* front */
  .front-brand{left:176px;top:52px}
  .hero-visual{left:88px;top:118px;width:362px;height:420px;
    clip-path:polygon(215px 0,362px 0,362px 420px,40px 420px,0 300px,0 190px,215px 190px);
    background:radial-gradient(ellipse at 72% 40%,#ffb33a 0%,#f59a17 38%,#fbd9a6 66%,rgba(255,255,255,0) 80%)}
  .headline{left:27px;top:222px;font-size:30px;line-height:36px;color:var(--grey-text);z-index:2}
  .headline strong{font-weight:700}
  .headline .accent{color:var(--orange)}
  .call{font-size:17px;font-weight:700;letter-spacing:1px;color:var(--grey-dark)}
  .call .accent{color:var(--orange);margin-right:4px}
  .front-call{left:29px;top:603px}
  .divider{width:2px;background:var(--rule)}
  .front-divider{left:275px;top:560px;height:104px}
  .address{left:292px;top:572px;font-size:13px;line-height:16.5px;color:var(--grey-dark);font-style:normal}
  .address b{font-weight:700;color:#555;font-size:13.5px}

  /* back */
  .tagline{left:35px;top:45px;font-size:13px;letter-spacing:1.3px;color:var(--grey-text)}
  .back-brand{left:333px;top:26px}
  .offer-panel{left:15px;top:91px;width:450px;height:315px;background:linear-gradient(180deg,var(--forest) 0%,var(--forest-deep) 100%)}
  .offer-band{left:0;top:405px;width:479px;height:190px;background:linear-gradient(180deg,var(--leaf) 0%,var(--leaf-light) 100%)}
  .offer-stripe{left:0;top:480px;width:479px;height:70px;background:linear-gradient(90deg,#c9c9c9 0%,#fff 12%,#fff 88%,#c9c9c9 100%)}
  .offer-title{left:113px;top:94px;width:250px;height:56px;background:var(--leaf);color:#fff;font-family:"Marcellus",Georgia,serif;font-size:26px;letter-spacing:1.5px;display:flex;align-items:center;justify-content:center}
  .only{left:3px;top:175px;width:157px;height:68px;background:var(--orange);color:#fff;font-family:"Titillium Web",Arial,sans-serif;font-weight:700;font-size:50px;line-height:68px;padding-left:26px}
  .rate-ghost{left:70px;top:215px;font-family:"Titillium Web",Arial,sans-serif;font-weight:900;font-size:150px;line-height:1;color:rgba(0,0,0,0.12)}
  .rate{left:22px;top:258px;font-family:"Titillium Web",Arial,sans-serif;font-weight:900;font-size:205px;line-height:1;letter-spacing:-4px;
    background:linear-gradient(180deg,#fff8dc 0%,#ffd64d 45%,#f7b51b 100%);-webkit-background-clip:text;background-clip:text;color:transparent;
    -webkit-text-stroke:3px #3a3a3a}
  .fee{left:158px;top:462px;width:162px;height:90px;background:#fff;border-radius:18px;color:var(--orange-deep);font-family:"Titillium Web",Arial,sans-serif;font-weight:700;font-size:64px;line-height:88px;text-align:center}
  .footnote{left:0;top:566px;width:479px;text-align:center;color:#fff;font-size:13px;letter-spacing:0.6px}
  .back-call{left:29px;top:629px}
  .back-divider{left:274px;top:608px;height:60px}
  .web{left:291px;top:630px;font-size:13px;color:var(--grey-dark)}
</style>
</head>
<body>
  <section class="page page--front" aria-label="Leaflet front">
    <div class="brand front-brand abs"><span class="brand__square"></span>halden</div>
    <div class="hero-visual abs" role="img" aria-label="Halved orange forming a telephone handset with a coiled cord, splashed with water"></div>
    <p class="headline abs">thinking of moving?<br><strong>call the <span class="accent">fresh one!</span></strong></p>
    <p class="call front-call abs"><span class="accent">call now</span> 01632 960418</p>
    <div class="divider front-divider abs"></div>
    <address class="address abs"><b>Halden Sales &amp; Lettings</b><br>12 Orchard Parade<br>Eastbury<br>EB4 7QT<br>www.haldenhomes.co.uk</address>
  </section>

  <section class="page page--back" aria-label="Leaflet back">
    <p class="tagline abs">market your home with reliable agent</p>
    <div class="brand back-brand abs"><span class="brand__square"></span>halden</div>
    <div class="offer-panel abs"></div>
    <div class="offer-band abs"></div>
    <div class="offer-stripe abs"></div>
    <div class="offer-title abs">SPECIAL OFFER</div>
    <div class="rate-ghost abs" aria-hidden="true">0.5%</div>
    <div class="only abs">only</div>
    <div class="rate abs">0.5%</div>
    <div class="fee abs">fee*</div>
    <p class="footnote abs">*for instructions received in March 2015</p>
    <p class="call back-call abs"><span class="accent">call now</span> 01632 960418</p>
    <div class="divider back-divider abs"></div>
    <p class="web abs">www.haldenhomes.co.uk</p>
  </section>
</body>
</html>
```